Copper Lantern Gin

The gin is 100% proof and men and anbody 18 - 30 year old will be a target market - the bottle is very distinctive and lends itself to a square label.

The bottle is curved with a large front face that lends itself to a striking design. There should be enough space around the label to show the black gin in the bottle as this is a feature.

The current bottle with the existing label is attached below as is the new glass bottle. The new gin will be coloured black.

Font styles to use
Decorative
Script

```html
<!DOCTYPE html>
<html lang="en">
<head>
<meta charset="utf-8">
<title>Copper Lantern Gin – Navy Strength Label</title>
<link rel="stylesheet" href="https://fonts.googleapis.com/css2?family=Poiret+One&family=UnifrakturMaguntia&family=Libre+Baskerville&display=swap">
<style>
  :root {
    --paper: #ffffff;
    --ink: #1a1a1a;
    --frame-dark: #2b2b2b;
    --frame-mid: #8a8a8a;
    --frame-light: #d9d9d9;
    --navy: #1b2028;
    --navy-deep: #12161c;
    --silver-top: #f4f4f4;
    --silver-bottom: #c9c9c9;
    --title: #b9c6d8;
    --art-light: #e6e6e6;
    --art-dark: #3a3a3a;
  }
  html, body {
    margin: 0;
    padding: 0;
    width: 1200px;
    height: 1200px;
    overflow: hidden;
    background: var(--paper);
  }
  .canvas {
    position: relative;
    width: 1200px;
    height: 1200px;
  }
  .crest-artwork {
    position: absolute;
    left: 390px;
    top: 90px;
    width: 420px;
    height: 340px;
    border-radius: 48% 48% 12% 12%;
    background: radial-gradient(ellipse at 50% 40%, var(--art-light) 0%, #a9a9a9 55%, var(--art-dark) 100%);
  }
  .label {
    position: absolute;
    left: 90px;
    top: 430px;
    width: 1020px;
    height: 600px;
    box-sizing: border-box;
    border: 6px solid var(--frame-dark);
    background: var(--frame-light);
    padding: 14px;
  }
  .label-inner {
    position: relative;
    width: 100%;
    height: 100%;
    box-sizing: border-box;
    border: 3px solid var(--frame-mid);
    outline: 2px solid var(--frame-dark);
    outline-offset: 6px;
    background: linear-gradient(var(--silver-top), var(--silver-bottom));
  }
  .title-band {
    position: absolute;
    left: 30px;
    right: 30px;
    top: 34px;
    height: 180px;
    background: linear-gradient(var(--navy), var(--navy-deep));
    border: 3px solid var(--frame-dark);
    display: flex;
    align-items: center;
    justify-content: center;
    padding-bottom: 20px;
    box-sizing: border-box;
  }
  .brand-name {
    margin: 0;
    font-family: "Poiret One", sans-serif;
    font-weight: 400;
    font-size: 100px;
    line-height: 1;
    letter-spacing: 4px;
    color: var(--title);
    text-transform: uppercase;
    white-space: nowrap;
  }
  .proof-badge {
    position: absolute;
    left: 50%;
    top: 174px;
    width: 80px;
    height: 80px;
    margin-left: -46px;
    border-radius: 50%;
    background: var(--paper);
    border: 6px solid var(--ink);
    display: flex;
    flex-direction: column;
    align-items: center;
    justify-content: center;
    font-family: "Libre Baskerville", serif;
    font-size: 15px;
    line-height: 1.15;
    color: var(--ink);
  }
  .style-line {
    position: absolute;
    left: 30px;
    right: 30px;
    top: 290px;
    display: flex;
    align-items: center;
    justify-content: center;
    gap: 22px;
  }
  .anchor-mark {
    width: 62px;
    height: 62px;
    flex: none;
  }
  .gin-style {
    margin: 0;
    font-family: "UnifrakturMaguntia", serif;
    font-size: 56px;
    line-height: 1;
    color: var(--ink);
    white-space: nowrap;
  }
  .rule {
    position: absolute;
    left: 160px;
    right: 160px;
    top: 400px;
    height: 2px;
    background: var(--ink);
  }
  .rule::after {
    content: "";
    position: absolute;
    left: 50%;
    top: -5px;
    width: 12px;
    height: 12px;
    margin-left: -6px;
    background: var(--ink);
    transform: rotate(45deg);
  }
  .name-plate {
    position: absolute;
    left: 50%;
    bottom: 22px;
    width: 220px;
    height: 34px;
    margin-left: -110px;
    border: 3px solid var(--frame-dark);
    border-radius: 17px;
    background: var(--paper);
  }
</style>
</head>
<body>
<main class="canvas">
  <div class="crest-artwork" role="img" aria-label="Decorative crest artwork in grey and white tones above the label"></div>

  <section class="label">
    <div class="label-inner">
      <div class="title-band">
        <h1 class="brand-name">Copper Lantern</h1>
      </div>

      <div class="proof-badge"><span>100%</span><span>Proof</span></div>

      <div class="style-line">
        <svg class="anchor-mark" viewBox="0 0 66 66" aria-hidden="true">
          <circle cx="33" cy="33" r="31" fill="#1a1a1a"/>
          <circle cx="33" cy="33" r="24" fill="#f0f0f0"/>
          <g fill="none" stroke="#1a1a1a" stroke-width="3" stroke-linecap="round">
            <circle cx="33" cy="19" r="3"/>
            <line x1="33" y1="22" x2="33" y2="48"/>
            <line x1="25" y1="27" x2="41" y2="27"/>
            <path d="M21 38 Q24 48 33 48 Q42 48 45 38"/>
          </g>
        </svg>
        <p class="gin-style">Navy Strength British Gin</p>
        <svg class="anchor-mark" viewBox="0 0 66 66" aria-hidden="true">
          <circle cx="33" cy="33" r="31" fill="#1a1a1a"/>
          <circle cx="33" cy="33" r="24" fill="#f0f0f0"/>
          <g fill="none" stroke="#1a1a1a" stroke-width="3" stroke-linecap="round">
            <circle cx="33" cy="19" r="3"/>
            <line x1="33" y1="22" x2="33" y2="48"/>
            <line x1="25" y1="27" x2="41" y2="27"/>
            <path d="M21 38 Q24 48 33 48 Q42 48 45 38"/>
          </g>
        </svg>
      </div>

      <div class="rule"></div>
      <div class="name-plate"></div>
    </div>
  </section>
</main>
</body>
</html>
```